Upscale business cards needed for Board of Directors

We need professional business cards created for members of our family business Board of Directors. We would like these relatively simple and straightforward, but also with a unique element to set them apart. Probably stick with neutral and simple colors - white, grey etc. We need space for the traditional elements, including name, title, address, email/phone number. And we will be creating several from this template so it needs to be template that is easy to switch information in and out of.
Business
See description

```html
<!DOCTYPE html>
<html lang="en">
<head>
<meta charset="utf-8">
<title>Keystone Holdings – Business Card</title>
<link rel="stylesheet" href="https://fonts.googleapis.com/css2?family=Roboto:wght@400;500;700&display=swap">
<style>
  :root {
    --backdrop: #e4e5e7;
    --card: #ffffff;
    --gold: #b59c6d;
    --ink: #1c1c1c;
    --band: #1a1a1a;
  }
  html, body {
    margin: 0;
    padding: 0;
    width: 1200px;
    height: 800px;
    overflow: hidden;
    background: var(--backdrop);
    font-family: "Roboto", Arial, sans-serif;
  }
  .canvas {
    position: relative;
    width: 1200px;
    height: 800px;
  }
  .card {
    position: absolute;
    left: 75px;
    top: 100px;
    width: 1050px;
    height: 600px;
    background: var(--card);
    overflow: hidden;
    box-shadow: 0 6px 24px rgba(0,0,0,0.12);
  }
  .card__top-band {
    position: absolute;
    left: 0; top: 0;
    width: 100%;
    height: 30px;
    background: var(--gold);
  }
  .card__bottom-band {
    position: absolute;
    left: 0; bottom: 0;
    width: 100%;
    height: 62px;
    background: var(--band);
  }
  .brand {
    position: absolute;
    left: 70px;
    top: 120px;
    display: flex;
    align-items: center;
    gap: 16px;
  }
  .brand__mark {
    width: 28px;
    height: 28px;
    background: var(--gold);
    flex: none;
  }
  .brand__name {
    font-size: 48px;
    font-weight: 700;
    color: var(--ink);
    line-height: 1;
    white-space: nowrap;
  }
  .contact {
    position: absolute;
    left: 70px;
    top: 280px;
    color: var(--ink);
    font-size: 23px;
    line-height: 30px;
  }
  .contact__address { margin: 0 0 4px; }
  .contact__line {
    display: flex;
    align-items: center;
    gap: 12px;
    white-space: nowrap;
  }
  .icon {
    width: 20px;
    height: 20px;
    flex: none;
  }
  .person {
    position: absolute;
    right: 70px;
    top: 320px;
    text-align: right;
  }
  .person__name {
    font-size: 27px;
    font-weight: 700;
    color: var(--ink);
    margin: 0;
  }
  .person__title {
    font-size: 22px;
    color: var(--gold);
    margin: 4px 0 0;
  }
  .phones {
    position: absolute;
    right: 70px;
    top: 420px;
    color: var(--ink);
    font-size: 24px;
    line-height: 31px;
  }
</style>
</head>
<body>
<div class="canvas">
  <div class="card">
    <div class="card__top-band"></div>

    <div class="brand">
      <span class="brand__mark" aria-hidden="true"></span>
      <span class="brand__name">Keystone Holdings</span>
    </div>

    <div class="contact">
      <p class="contact__address">48 Harbor Lane, Suite 210<br>City, State, Zip Code</p>
      <div class="contact__line">
        <svg class="icon" viewBox="0 0 20 20" aria-hidden="true">
          <rect width="20" height="20" rx="2" fill="var(--gold)"/>
          <rect x="4" y="6" width="12" height="8" fill="none" stroke="#fff" stroke-width="1.5"/>
          <path d="M4 6 L10 11 L16 6" fill="none" stroke="#fff" stroke-width="1.5"/>
        </svg>
        <span>dreeve@keystoneholdings.com</span>
      </div>
      <div class="contact__line">
        <svg class="icon" viewBox="0 0 20 20" aria-hidden="true">
          <rect width="20" height="20" rx="2" fill="var(--gold)"/>
          <circle cx="10" cy="10" r="6" fill="none" stroke="#fff" stroke-width="1.5"/>
          <path d="M4 10 H16 M10 4 V16" stroke="#fff" stroke-width="1.2"/>
        </svg>
        <span>keystoneholdings.com</span>
      </div>
    </div>

    <div class="person">
      <p class="person__name">DANIEL REEVE</p>
      <p class="person__title">Managing director</p>
    </div>

    <div class="phones">
      <div class="contact__line">
        <svg class="icon" viewBox="0 0 20 20" aria-hidden="true">
          <rect width="20" height="20" rx="2" fill="var(--gold)"/>
          <path d="M6 4 L8.5 4 L9.5 7 L8 8.5 C9 10.5 10 11.5 11.5 12 L13 10.5 L16 11.5 L16 14 C11 15 5 9 6 4 Z" fill="#fff"/>
        </svg>
        <span>0781-5520-4139</span>
      </div>
      <div class="contact__line">
        <svg class="icon" viewBox="0 0 20 20" aria-hidden="true">
          <rect width="20" height="20" rx="2" fill="var(--gold)"/>
          <rect x="6" y="3" width="8" height="14" rx="1.5" fill="none" stroke="#fff" stroke-width="1.5"/>
          <circle cx="10" cy="14.5" r="1" fill="#fff"/>
        </svg>
        <span>0735-9016-2284</span>
      </div>
    </div>

    <div class="card__bottom-band"></div>
  </div>
</div>
</body>
</html>
```